Dental Medical History Form - Content provided

Design a medical history form for a dental practice. Content is provided so all that is needed is the formatting to make it look great and easy to read.

"Patient Information" to include all information contained in top portion of the "Patient Medical History Form" docx file.

"Medical History" should follow the formatting and content of the "Exact Medical History" file as this is what the entry fields look like in our practice software and so we would like it to match.

1st page - Patient info, allergies, medications, antibiotics, joint replacement, pregnancy.

2nd page - Do you have, or have you had, any of the following? . . . . . . .

Target Market(s)

All ages but must be clear enough for elderly to read. Use as much space as possible to keep font size bigger yet keep to two pages

Industry/Entity Type

Dental

Font styles to use
Sans Serif

Requirements
Must have
• All content provided
• Our logo at the top (file provided)
• Century Gothic Font
• Limit to two pages

```html
<!DOCTYPE html>
<html lang="en">
<head>
<meta charset="utf-8">
<title>Harbourline Dental – Confidential Medical History</title>
<link href="https://fonts.googleapis.com/css2?family=Jost:wght@400;500;600&display=swap" rel="stylesheet">
<style>
:root{
  --ink:#2f3338;
  --muted:#6d7780;
  --brand:#4c5b69;
  --footer:#8b9aa7;
  --sage:#d5ddd4;
  --field:#e1e6ea;
  --box:#dde2e6;
  --page:#ffffff;
  --bg:#ffffff;
  --edge:#e4e6e8;
}
*{box-sizing:border-box;margin:0;padding:0}
html,body{width:1200px;height:1200px;overflow:hidden;background:var(--bg)}
body{font-family:"Jost",sans-serif;color:var(--ink);font-size:10.5px;line-height:1.2}
.canvas{position:relative;width:1200px;height:1200px}
.page{position:absolute;top:190px;width:576px;height:815px;background:var(--page);border:1px solid var(--edge);box-shadow:0 2px 10px rgba(0,0,0,.08);overflow:hidden}
.page--info{left:12px}
.page--history{left:612px}

/* page 1 */
.masthead{position:relative;height:120px}
.masthead__band{position:absolute;left:0;right:0;top:28px;height:22px;background:var(--sage)}
.brand{position:absolute;left:34px;top:14px;font-size:24px;font-weight:400;color:var(--brand);letter-spacing:.5px;background:var(--page);padding-right:10px}
.title-band{position:absolute;left:0;right:0;top:80px;height:30px;background:var(--sage);display:flex;align-items:center;justify-content:center}
.title{font-size:17px;font-weight:400;letter-spacing:.6px}
.sheet{padding:10px 30px 0}
.info{display:grid;grid-template-columns:1fr 1fr;gap:18px}
.line{display:flex;align-items:center;gap:5px;margin-bottom:5px;white-space:nowrap}
.line .field{flex:1}
.field{display:inline-block;height:12px;background:var(--field)}
.sub{display:flex;justify-content:space-around;font-size:7.5px;color:var(--muted);margin:-3px 0 5px 34px}
.spacer{height:10px}
.q{font-weight:600;font-size:11px;margin:12px 0 6px}
.opts{display:flex;flex-wrap:wrap;gap:4px 12px;align-items:center;margin-bottom:4px}
.opt{display:inline-flex;align-items:center;gap:3px}
.box{display:inline-block;width:9px;height:9px;background:var(--box)}
.tick{font-size:10px}
.meds{display:grid;grid-template-columns:repeat(3,1fr);gap:6px 10px}
.meds .field{width:100%}
.yn{display:inline-flex;align-items:center;gap:3px;white-space:nowrap;font-size:10px}
.yn .box{margin-right:4px}
.qrow{display:flex;align-items:center;justify-content:space-between;margin-bottom:5px}
.qrow strong{font-weight:600}
.footer{position:absolute;left:30px;right:30px;bottom:22px;display:flex;justify-content:space-between;color:var(--footer);font-size:10px}
.footer .sep{color:var(--brand)}

/* page 2 */
.history{padding:32px 28px 0}
.history__q{font-weight:600;font-size:12px;margin-bottom:10px}
.cols{display:grid;grid-template-columns:1fr 1fr;gap:22px}
.group{margin-bottom:8px}
.group h3{font-size:10.5px;font-weight:600;margin-bottom:3px}
.item{display:flex;justify-content:space-between;align-items:center;height:15.5px;font-size:10px}
.sign{margin-top:10px;display:grid;grid-template-columns:1fr 1fr;gap:22px}
.sign .line{margin-bottom:7px}
.thanks{margin-top:12px;font-size:9.5px;color:var(--ink);line-height:1.35}
</style>
</head>
<body>
<div class="canvas">

  <section class="page page--info">
    <header class="masthead">
      <div class="masthead__band"></div>
      <div class="brand">Harbourline Dental</div>
      <div class="title-band"><h1 class="title">CONFIDENTIAL MEDICAL HISTORY</h1></div>
    </header>

    <div class="sheet">
      <div class="info">
        <div class="patient">
          <div class="line">Name: <span class="field"></span></div>
          <div class="sub"><span>Title</span><span>First</span><span>Middle</span><span>Last</span></div>
          <div class="line">Address: <span class="field"></span></div>
          <div class="line">DOB: <span class="field"></span></div>
          <div class="line">Email Address: <span class="field"></span></div>
          <div class="line">Phone Number(s): <span class="field"></span></div>
          <div class="sub"><span>Mobile</span><span>Work</span><span>Home</span></div>
          <div class="spacer"></div>
          <div class="line">Emergency Contact Person:</div>
          <div class="line">Name: <span class="field"></span></div>
          <div class="line">Relationship: <span class="field"></span></div>
          <div class="line">Phone number: <span class="field"></span></div>
        </div>
        <div class="practice">
          <div class="line">General Practitioner:</div>
          <div class="line">Name: <span class="field"></span></div>
          <div class="line">Practice Name: <span class="field"></span></div>
          <div class="line">Phone Number: <span class="field"></span></div>
          <div class="line">Do you have a health fund with dental cover?</div>
          <div class="line"><span class="yn">Yes <span class="box"></span> or No <span class="box"></span></span></div>
          <div class="line">If so, what is the name of the fund? <span class="field"></span></div>
          <div class="line">Fund Number: <span class="field"></span></div>
          <div class="line">Priority Number on card: 0 1 2 3 4 5 <span class="field"></span></div>
          <div class="line">Occupation: <span class="field"></span></div>
          <div class="line">Referred by: <span class="field"></span></div>
        </div>
      </div>

      <p class="q">Please indicate if you are allergic to any of the following <span class="tick">✓</span>?</p>
      <div class="opts">
        <span class="opt">Aspirin <span class="box"></span></span>
        <span class="opt">Codeine <span class="box"></span></span>
        <span class="opt">Penicillin <span class="box"></span></span>
        <span class="opt">Sulfites <span class="box"></span></span>
        <span class="opt">Latex <span class="box"></span></span>
        <span class="opt">Local Anaesthetic <span class="box"></span></span>
        <span class="opt">Lactose <span class="box"></span></span>
        <span class="opt">Nickel <span class="box"></span></span>
      </div>
      <div class="line">Other <span class="field"></span></div>

      <p class="q">Are you currently taking, or have ever taken, any of the following medication <span class="tick">✓</span>?</p>
      <div class="opts">
        <span class="opt">Asthma inhaler <span class="box"></span></span>
        <span class="opt">Anti-epileptics <span class="box"></span></span>
        <span class="opt">Anti-depressants <span class="box"></span></span>
        <span class="opt">Blood Pressure <span class="box"></span></span>
        <span class="opt">Blood Thinners <span class="box"></span></span>
        <span class="opt">Bisphosphonates <span class="box"></span></span>
        <span class="opt">Chemotherapy <span class="box"></span></span>
        <span class="opt">Insulin <span class="box"></span></span>
        <span class="opt">Immunosuppressants <span class="box"></span></span>
        <span class="opt">Steroids <span class="box"></span></span>
        <span class="opt">Oral Contraceptive <span class="box"></span></span>
        <span class="opt">Other <span class="box"></span></span>
      </div>

      <p class="q">Please specify medication name, dose, and frequency where possible:</p>
      <div class="meds">
        <span class="field"></span><span class="field"></span><span class="field"></span>
        <span class="field"></span><span class="field"></span><span class="field"></span>
        <span class="field"></span><span class="field"></span><span class="field"></span>
      </div>

      <div class="spacer"></div>
      <div class="qrow"><strong>Do you require antibiotic cover?</strong><span class="yn">Yes <span class="box"></span> No <span class="box"></span></span></div>
      <div class="qrow"><strong>Have you had a joint replacement?</strong><span class="yn">Yes <span class="box"></span> No <span class="box"></span> Possible <span class="box"></span></span></div>
      <div class="spacer"></div>
      <div class="line">Women:</div>
      <div class="qrow"><strong>Are you pregnant?</strong><span class="yn">Yes <span class="box"></span> No <span class="box"></span></span></div>
      <div class="qrow"><span>or <strong>Breast Feeding?</strong></span><span class="yn">Yes <span class="box"></span> No <span class="box"></span></span></div>
    </div>

    <footer class="footer">
      <span>Harbourline Dental</span><span class="sep">|</span>
      <span>Suite 4/18 Seaview Rd</span><span class="sep">|</span>
      <span>Kinross NSW 2260</span><span class="sep">|</span>
      <span>(02) 4000 1234</span>
    </footer>
  </section>

  <section class="page page--history">
    <div class="history">
      <p class="history__q">Do you have, or have you had, any of the following?</p>
      <div class="cols">
        <div>
          <div class="group">
            <h3>Dental</h3>
            <div class="item">Acid Reflux<span class="yn">Yes <span class="box"></span> No <span class="box"></span></span></div>
            <div class="item">Bad Breath/Taste<span class="yn">Yes <span class="box"></span> No <span class="box"></span></span></div>
            <div class="item">Bleeding/Swollen/Sore Gums<span class="yn">Yes <span class="box"></span> No <span class="box"></span></span></div>
            <div class="item">Blisters/Ulcers in Mouth<span class="yn">Yes <span class="box"></span> No <span class="box"></span></span></div>
            <div class="item">Broken tooth/filling<span class="yn">Yes <span class="box"></span> No <span class="box"></span></span></div>
            <div class="item">Burning tongue<span class="yn">Yes <span class="box"></span> No <span class="box"></span></span></div>
            <div class="item">Dry mouth<span class="yn">Yes <span class="box"></span> No <span class="box"></span></span></div>
            <div class="item">Food collection between teeth<span class="yn">Yes <span class="box"></span> No <span class="box"></span></span></div>
            <div class="item">Grinding/clenching teeth (day/night)<span class="yn">Yes <span class="box"></span> No <span class="box"></span></span></div>
            <div class="item">Loose teeth<span class="yn">Yes <span class="box"></span> No <span class="box"></span></span></div>
            <div class="item">Crooked teeth<span class="yn">Yes <span class="box"></span> No <span class="box"></span></span></div>
            <div class="item">Discoloured teeth<span class="yn">Yes <span class="box"></span> No <span class="box"></span></span></div>
            <div class="item">Sensitivity to Hot/Cold<span class="yn">Yes <span class="box"></span> No <span class="box"></span></span></div>
            <div class="item">Pain when chewing<span class="yn">Yes <span class="box"></span> No <span class="box"></span></span></div>
            <div class="item">Jaw pain/Fracture<span class="yn">Yes <span class="box"></span> No <span class="box"></span></span></div>
            <div class="item">Orthodontic treatment/history<span class="yn">Yes <span class="box"></span> No <span class="box"></span></span></div>
            <div class="item">Other<span class="yn">Yes <span class="box"></span> No <span class="box"></span></span></div>
          </div>
          <div class="group">
            <h3>Lifestyle</h3>
            <div class="item">More than one glass alcohol per day<span class="yn">Yes <span class="box"></span> No <span class="box"></span></span></div>
            <div class="item">Smoker<span class="yn">Yes <span class="box"></span> No <span class="box"></span></span></div>
            <div class="item">Vaping<span class="yn">Yes <span class="box"></span> No <span class="box"></span></span></div>
            <div class="item">Recreational drugs<span class="yn">Yes <span class="box"></span> No <span class="box"></span></span></div>
          </div>
          <div class="group">
            <h3>Infections</h3>
            <div class="item">Hepatitis A/B/C<span class="yn">Yes <span class="box"></span> No <span class="box"></span></span></div>
            <div class="item">HIV/AIDS<span class="yn">Yes <span class="box"></span> No <span class="box"></span></span></div>
            <div class="item">Herpes/Cold sores<span class="yn">Yes <span class="box"></span> No <span class="box"></span></span></div>
            <div class="item">Glandular fever<span class="yn">Yes <span class="box"></span> No <span class="box"></span></span></div>
            <div class="item">Rheumatic fever<span class="yn">Yes <span class="box"></span> No <span class="box"></span></span></div>
            <div class="item">Tuberculosis<span class="yn">Yes <span class="box"></span> No <span class="box"></span></span></div>
          </div>
        </div>
        <div>
          <div class="group">
            <h3>Heart</h3>
            <div class="item">Angina<span class="yn">Yes <span class="box"></span> No <span class="box"></span></span></div>
            <div class="item">Atrial Fibrillation<span class="yn">Yes <span class="box"></span> No <span class="box"></span></span></div>
            <div class="item">Blood Pressure (High/Low)<span class="yn">Yes <span class="box"></span> No <span class="box"></span></span></div>
            <div class="item">Congenital Heart Disease<span class="yn">Yes <span class="box"></span> No <span class="box"></span></span></div>
            <div class="item">Heart attack<span class="yn">Yes <span class="box"></span> No <span class="box"></span></span></div>
            <div class="item">Heart murmur<span class="yn">Yes <span class="box"></span> No <span class="box"></span></span></div>
            <div class="item">Heart surgery<span class="yn">Yes <span class="box"></span> No <span class="box"></span></span></div>
            <div class="item">Heart valve replacement<span class="yn">Yes <span class="box"></span> No <span class="box"></span></span></div>
            <div class="item">Infective endocarditis<span class="yn">Yes <span class="box"></span> No <span class="box"></span></span></div>
            <div class="item">Rheumatic Heart Disease<span class="yn">Yes <span class="box"></span> No <span class="box"></span></span></div>
            <div class="item">Pacemaker<span class="yn">Yes <span class="box"></span> No <span class="box"></span></span></div>
            <div class="item">Stent<span class="yn">Yes <span class="box"></span> No <span class="box"></span></span></div>
          </div>
          <div class="group">
            <h3>Other</h3>
            <div class="item">Anxiety/PTSD<span class="yn">Yes <span class="box"></span> No <span class="box"></span></span></div>
            <div class="item">Arthritis<span class="yn">Yes <span class="box"></span> No <span class="box"></span></span></div>
            <div class="item">Alzheimer's<span class="yn">Yes <span class="box"></span> No <span class="box"></span></span></div>
            <div class="item">Asthma<span class="yn">Yes <span class="box"></span> No <span class="box"></span></span></div>
            <div class="item">Anaphylaxis<span class="yn">Yes <span class="box"></span> No <span class="box"></span></span></div>
            <div class="item">Auto-immune disease<span class="yn">Yes <span class="box"></span> No <span class="box"></span></span></div>
            <div class="item">Coeliac<span class="yn">Yes <span class="box"></span> No <span class="box"></span></span></div>
            <div class="item">Depression<span class="yn">Yes <span class="box"></span> No <span class="box"></span></span></div>
            <div class="item">Diabetes<span class="yn">Yes <span class="box"></span> No <span class="box"></span></span></div>
            <div class="item">Epilepsy<span class="yn">Yes <span class="box"></span> No <span class="box"></span></span></div>
            <div class="item">Kidney Disease<span class="yn">Yes <span class="box"></span> No <span class="box"></span></span></div>
            <div class="item">Liver Disease<span class="yn">Yes <span class="box"></span> No <span class="box"></span></span></div>
            <div class="item">Osteoporosis<span class="yn">Yes <span class="box"></span> No <span class="box"></span></span></div>
            <div class="item">Parkinson's<span class="yn">Yes <span class="box"></span> No <span class="box"></span></span></div>
            <div class="item">Radiation to Head/Neck<span class="yn">Yes <span class="box"></span> No <span class="box"></span></span></div>
            <div class="item">Schizophrenia<span class="yn">Yes <span class="box"></span> No <span class="box"></span></span></div>
            <div class="item">Snoring<span class="yn">Yes <span class="box"></span> No <span class="box"></span></span></div>
            <div class="item">Sleep apnea<span class="yn">Yes <span class="box"></span> No <span class="box"></span></span></div>
            <div class="item">Stroke<span class="yn">Yes <span class="box"></span> No <span class="box"></span></span></div>
          </div>
        </div>
      </div>

      <div class="sign">
        <div>
          <div class="line">Signature: <span class="field"></span></div>
          <div class="line">Date: <span class="field"></span></div>
        </div>
        <div>
          <div class="line">Other: <span class="field"></span></div>
        </div>
      </div>

      <p class="thanks">Thank you for the time to complete your medical history form. Oral health is linked to overall health and this comprehensive questionnaire will help us to provide you with optimal and safe care.</p>
    </div>
  </section>

</div>
</body>
</html>
```